Veltrona Cabinets Letter Head and Email Signature

Hi
I would love a design package for a letterhead, email signature, even update my business card if you like if you can come up with a great idea for my new high end cabinet shop. Veltrona Cabinets brings timeless craftsmanship to modern interiors, specializing in high end, custom cabinetry designed for architects and interior designers.

Target Market(s)

high end, luxury market

Industry/Entity Type

cabinet making

Requirements
Must have
• my colours of logo as the theme

```html
<!DOCTYPE html>
<html lang="en">
<head>
<meta charset="utf-8">
<title>Veltrona Cabinets – Stationery</title>
<link rel="stylesheet" href="https://fonts.googleapis.com/css2?family=Montserrat:wght@400;500;600&family=Karla:wght@400;500&display=swap">
<style>
  :root {
    --green: #4a7c4e;
    --ink: #222324;
    --paper: #ffffff;
    --backdrop: #6a3f22;
    --pattern: #f3f3f2;
    --label: #fbf3ea;
  }
  * { box-sizing: border-box; margin: 0; padding: 0; }
  html, body { width: 1131px; height: 1200px; overflow: hidden; }
  body {
    position: relative;
    background: var(--backdrop);
    font-family: "Montserrat", sans-serif;
    color: var(--ink);
  }
  .section-label {
    position: absolute;
    color: var(--label);
    font-size: 16px;
    font-weight: 500;
    letter-spacing: 0.3px;
  }
  .label-letterhead { left: 60px; top: 28px; }
  .label-card { right: 89px; top: 154px; }
  .label-email { left: 70px; top: 1089px; }

  .wordmark {
    font-family: "Montserrat", sans-serif;
    font-weight: 600;
    color: var(--green);
    white-space: nowrap;
    letter-spacing: 0.2px;
  }
  .wordmark.on-green { color: var(--paper); }

  .icon { width: 9px; height: 9px; flex: none; }
  .contact-list { list-style: none; }
  .contact-list li { display: flex; align-items: center; gap: 6px; }

  /* Letterhead */
  .letterhead {
    position: absolute; left: 58px; top: 68px; width: 603px; height: 780px;
    background: var(--paper);
  }
  .letterhead .wordmark { position: absolute; left: 22px; top: 38px; font-size: 19px; }
  .letterhead .contact-list {
    position: absolute; right: 16px; top: 22px; font-size: 8px; text-align: right;
  }
  .letterhead .contact-list li { justify-content: flex-end; height: 17px; }
  .letterhead .accent-rule {
    position: absolute; left: 599px; top: 16px; width: 2px; height: 60px; background: var(--green);
  }
  .letterhead .footer { position: absolute; left: 0; bottom: 0; width: 603px; height: 43px; }
  .letterhead .tagline {
    position: absolute; right: 17px; bottom: 16px; color: var(--paper); font-size: 12px; font-weight: 500;
  }

  /* Cards */
  .card {
    position: absolute; width: 297px; height: 169px; border-radius: 7px; overflow: hidden;
    background: var(--paper);
  }
  .card-front { left: 750px; top: 191px; }
  .card-front .wordmark { position: absolute; left: 12px; top: 24px; font-size: 13px; }
  .card-front .holder { position: absolute; right: 12px; top: 18px; text-align: right; }
  .holder-name { font-size: 12px; font-weight: 600; color: var(--green); }
  .holder-role { font-size: 6.5px; font-weight: 500; }
  .card-front .contact-list { position: absolute; left: 12px; top: 86px; font-size: 8px; }
  .card-front .contact-list li,
  .signature .contact-list li { height: 17.5px; }
  .card-footer { position: absolute; left: 0; bottom: 0; width: 100%; height: 25px; }
  .card-tagline {
    position: absolute; bottom: 6px; color: var(--paper);
    font-family: "Karla", sans-serif; font-size: 9px; letter-spacing: 0.3px;
  }
  .card-front .card-tagline { left: 160px; }

  .card-back-green {
    left: 751px; top: 369px; background: var(--green);
    display: flex; align-items: center; justify-content: center;
  }
  .card-back-green .wordmark { font-size: 22px; }

  .card-back-pattern { left: 762px; top: 559px; }
  .card-back-pattern .pattern-field {
    position: absolute; inset: 0; background: var(--pattern);
  }
  .card-back-pattern .wordmark {
    position: absolute; left: 0; right: 0; top: 72px; text-align: center; font-size: 22px;
  }

  /* Email signature */
  .signature { left: 67px; top: 903px; width: 355px; height: 169px; }
  .signature .holder { position: absolute; left: 17px; top: 13px; }
  .signature .holder-name { font-size: 12px; }
  .signature .holder-role { font-size: 7.5px; }
  .signature .contact-list { position: absolute; left: 17px; top: 38px; font-size: 8px; }
  .signature .wordmark { position: absolute; left: 17px; top: 110px; font-size: 14px; }
  .signature .card-tagline { left: 217px; }
</style>
</head>
<body>
<svg width="0" height="0" style="position:absolute" aria-hidden="true">
  <defs>
    <symbol id="icon-phone" viewBox="0 0 10 10">
      <circle cx="5" cy="5" r="4.4" fill="none" stroke="#4a7c4e" stroke-width="0.9"/>
      <path d="M3.6 2.6 L4.5 3.4 L4 4.2 Q4.6 5.6 5.8 6.1 L6.6 5.5 L7.4 6.4 L6.6 7.3 Q3.6 6.6 2.8 3.4 Z" fill="#4a7c4e"/>
    </symbol>
    <symbol id="icon-mail" viewBox="0 0 10 10">
      <path d="M1 4 L5 1.6 L9 4 L9 8.4 L1 8.4 Z" fill="#4a7c4e"/>
      <path d="M1.6 4.2 L5 6.3 L8.4 4.2" fill="none" stroke="#fff" stroke-width="0.8"/>
    </symbol>
    <symbol id="icon-social" viewBox="0 0 10 10">
      <rect x="1" y="1" width="8" height="8" rx="2" fill="none" stroke="#4a7c4e" stroke-width="0.9"/>
    </symbol>
  </defs>
</svg>

<div class="section-label label-letterhead">Letterhead</div>
<div class="section-label label-card">Business Card</div>
<div class="section-label label-email">Email Signature</div>

<section class="letterhead">
  <div class="wordmark">Veltrona Cabinets</div>
  <ul class="contact-list">
    <li>040 555 0182 <svg class="icon"><use href="#icon-phone"/></svg></li>
    <li>info@veltronacabinets.com.au <svg class="icon"><use href="#icon-mail"/></svg></li>
    <li>@veltrona.cabinets <svg class="icon"><use href="#icon-social"/></svg></li>
  </ul>
  <div class="accent-rule"></div>
  <svg class="footer" viewBox="0 0 603 43" aria-hidden="true">
    <path d="M0 31 L350 31 Q360 31 368 24 L384 8 Q392 0 404 0 L603 0 L603 43 L0 43 Z" fill="#222324"/>
    <path d="M0 18 L354 18 L346 27 L0 27 Z" fill="#4a7c4e"/>
  </svg>
  <div class="tagline">Timeless Craft. Modern Interiors.</div>
</section>

<section class="card card-front">
  <div class="wordmark">Veltrona Cabinets</div>
  <div class="holder">
    <div class="holder-name">Miles Varrick</div>
    <div class="holder-role">Director Craftsman</div>
  </div>
  <ul class="contact-list">
    <li><svg class="icon"><use href="#icon-phone"/></svg> 040 555 0182</li>
    <li><svg class="icon"><use href="#icon-mail"/></svg> info@veltronacabinets.com.au</li>
    <li><svg class="icon"><use href="#icon-social"/></svg> @veltrona.cabinets</li>
  </ul>
  <svg class="card-footer" viewBox="0 0 297 25" aria-hidden="true">
    <path d="M0 11 L128 11 L139 0 L297 0 L297 25 L0 25 Z" fill="#222324"/>
    <path d="M0 1 L134 1 L127 8.5 L0 8.5 Z" fill="#4a7c4e"/>
  </svg>
  <div class="card-tagline">Build from First Principles</div>
</section>

<section class="card card-back-green">
  <div class="wordmark on-green">Veltrona Cabinets</div>
</section>

<section class="card card-back-pattern">
  <div class="pattern-field" role="img" aria-label="Faint repeating pattern of the brand mark across the card"></div>
  <div class="wordmark">Veltrona Cabinets</div>
</section>

<section class="card signature">
  <div class="holder">
    <span class="holder-name">Miles Varrick,</span><span class="holder-role"> Director Craftsman</span>
  </div>
  <ul class="contact-list">
    <li><svg class="icon"><use href="#icon-phone"/></svg> 040 555 0182</li>
    <li><svg class="icon"><use href="#icon-mail"/></svg> info@veltronacabinets.com.au</li>
    <li><svg class="icon"><use href="#icon-social"/></svg> @veltrona.cabinets</li>
  </ul>
  <div class="wordmark">Veltrona Cabinets</div>
  <svg class="card-footer" viewBox="0 0 355 21" aria-hidden="true" style="height:21px">
    <path d="M0 9 L126 9 L137 0 L355 0 L355 21 L0 21 Z" fill="#222324"/>
    <path d="M0 1 L133 1 L126 6.5 L0 6.5 Z" fill="#4a7c4e"/>
  </svg>
  <div class="card-tagline" style="bottom:5px">Build from First Principles</div>
</section>
</body>
</html>
```